Family Brewery needs a label design for the four different types of beer.

We need a label design for two beer bottle sizes (500 and 700 ml. )
The label design should include the family monogram and company logo, as it would be a corporate gift for the new year from our CEO to business partners and clients. We have one request for showing the company logo on bottle. As it would be the new year edition, we would like to see design "adaptive" in case we would like to keep it after the holidays on an ongoing basis. Our main company direction is design and manufacture of cooling equipment for ice rinks, so it would be fine but not necessary to see design related to our business (if you would like to check the company, there is our website - www.kelvana.ru)
Labels on bottles should be in the same style but vary depending on the variety and taste of beer.
Types of bear
-Pilzner ( 4.4 % of alcohol)
-Honig Pilsner(5.2 % of alcohol)
-Wiener Ale ( 4.7 % of alcohol)
-Weissbier (5.6 % of alcohol)
If you have any questions just message me and i will answer as soon as possible.
Files attached contain the family monogram, company logo ( kelvana ), picture of beer bottles that would be in usage.

```html
<!DOCTYPE html>
<html lang="en">
<head>
<meta charset="utf-8">
<title>Kelvana-L Family Brewery — Beer Labels</title>
<link href="https://fonts.googleapis.com/css2?family=Oswald:wght@300;500;600&display=swap" rel="stylesheet">
<style>
  :root {
    --canvas: #ebeceb;
    --gold: #a88e5e;
    --navy: #12151f;
    --paper: #ffffff;
    --wine: #5e0c0e;
    --pine: #083a2e;
    --black: #111111;
    --white: #ffffff;
  }
  * { margin: 0; padding: 0; box-sizing: border-box; }
  html, body { width: 1200px; height: 1200px; overflow: hidden; background: var(--canvas); }
  .sheet { position: relative; width: 1200px; height: 1200px; }
  .label { position: absolute; width: 390px; height: 442px; overflow: visible; }
  .label--pilzner { left: 105px; top: 76px;  --bg: var(--navy);  --ink: var(--gold);  --mark: var(--gold); }
  .label--honig   { left: 705px; top: 78px;  --bg: var(--paper); --ink: var(--black); --mark: var(--gold); }
  .label--wiener  { left: 105px; top: 675px; --bg: var(--wine);  --ink: var(--white); --mark: var(--white); }
  .label--weiss   { left: 705px; top: 677px; --bg: var(--pine);  --ink: var(--white); --mark: var(--white); }

  .label__body { fill: var(--bg); }
  .label__rule { fill: none; stroke: var(--gold); stroke-width: 1.6; }
  .label__rule--thin { stroke-width: 1; }
  .label__ornament { fill: var(--gold); opacity: 0.35; }
  .label__arc-text { font-family: "Oswald", sans-serif; font-weight: 600; fill: var(--ink); }
  .label__brewery { font-size: 28px; }
  .label__variety { font-size: 36px; }
  .label__title { font-family: "Oswald", sans-serif; font-weight: 500; font-size: 93px; fill: var(--gold); }
  .label__spec { font-family: "Oswald", sans-serif; font-weight: 300; fill: var(--gold); font-size: 17px; }
  .label__spec-small { font-size: 10px; }
  .label__brand-ring { fill: var(--bg); stroke: var(--mark); stroke-width: 2; }
  .label__brand-name { font-family: "Oswald", sans-serif; font-weight: 500; font-size: 13px; letter-spacing: 1px; fill: var(--mark); }
</style>
</head>
<body>
<main class="sheet">

  <svg width="0" height="0" style="position:absolute">
    <defs>
      <path id="arc-top" d="M -215 62 A 215 215 0 0 1 215 62"/>
      <path id="arc-bottom" d="M -215 -31 A 215 215 0 0 0 215 -31"/>
    </defs>
  </svg>

  <!-- Pilzner -->
  <svg class="label label--pilzner" viewBox="-195 -221 390 442" aria-label="Kelvana-L Pilzner label">
    <path class="label__body" d="M -195 -104 A 221 221 0 0 1 195 -104 L 195 104 A 221 221 0 0 1 -195 104 Z"/>
    <path class="label__rule" d="M -169 -107 A 200 200 0 0 1 169 -107"/>
    <path class="label__rule label__rule--thin" d="M -162 -107 A 194 194 0 0 1 162 -107"/>
    <path class="label__rule label__rule--thin" d="M -80 -107 A 134 134 0 0 1 80 -107"/>
    <path class="label__rule" d="M -173 101 A 200 200 0 0 0 173 101"/>
    <path class="label__rule label__rule--thin" d="M -166 101 A 194 194 0 0 0 166 101"/>
    <path class="label__rule label__rule--thin" d="M -91 101 A 134 134 0 0 0 91 101"/>
    <text class="label__arc-text label__brewery"><textPath href="#arc-top" startOffset="50%" text-anchor="middle" textLength="240" lengthAdjust="spacing">FAMILY BREWERY</textPath></text>
    <rect class="label__rule" x="-176" y="-107" width="352" height="48"/>
    <rect class="label__rule label__rule--thin" x="-166" y="-100" width="332" height="34"/>
    <g role="img" aria-label="Crown, family monogram and foliate scroll ornament">
      <rect class="label__ornament" x="-135" y="-96" width="270" height="26"/>
      <circle class="label__ornament" cx="0" cy="-76" r="32"/>
      <rect class="label__ornament" x="-14" y="-135" width="28" height="16"/>
    </g>
    <text class="label__title" x="0" y="25" text-anchor="middle" textLength="345" lengthAdjust="spacingAndGlyphs">Кельвана-Л</text>
    <rect class="label__rule" x="-176" y="49" width="352" height="52"/>
    <rect class="label__rule label__rule--thin" x="-166" y="56" width="332" height="38"/>
    <text class="label__spec" x="-94" y="80" text-anchor="middle">500 ml</text>
    <text class="label__spec" x="50" y="80">4.4 % <tspan class="label__spec-small">of alcohol</tspan></text>
    <circle class="label__brand-ring" cx="0" cy="94" r="40"/>
    <text class="label__brand-name" x="0" y="99" text-anchor="middle">KELVANA</text>
    <text class="label__arc-text label__variety"><textPath href="#arc-bottom" startOffset="50%" text-anchor="middle" textLength="226" lengthAdjust="spacingAndGlyphs">Kelvana-L | Pilzner</textPath></text>
  </svg>

  <!-- Honig Pilsner -->
  <svg class="label label--honig" viewBox="-195 -221 390 442" aria-label="Kelvana-L Honig Pilsner label">
    <path class="label__body" d="M -195 -104 A 221 221 0 0 1 195 -104 L 195 104 A 221 221 0 0 1 -195 104 Z"/>
    <path class="label__rule" d="M -169 -107 A 200 200 0 0 1 169 -107"/>
    <path class="label__rule label__rule--thin" d="M -162 -107 A 194 194 0 0 1 162 -107"/>
    <path class="label__rule label__rule--thin" d="M -80 -107 A 134 134 0 0 1 80 -107"/>
    <path class="label__rule" d="M -173 101 A 200 200 0 0 0 173 101"/>
    <path class="label__rule label__rule--thin" d="M -166 101 A 194 194 0 0 0 166 101"/>
    <path class="label__rule label__rule--thin" d="M -91 101 A 134 134 0 0 0 91 101"/>
    <text class="label__arc-text label__brewery"><textPath href="#arc-top" startOffset="50%" text-anchor="middle" textLength="240" lengthAdjust="spacing">FAMILY BREWERY</textPath></text>
    <rect class="label__rule" x="-176" y="-107" width="352" height="48"/>
    <rect class="label__rule label__rule--thin" x="-166" y="-100" width="332" height="34"/>
    <g role="img" aria-label="Crown, family monogram and foliate scroll ornament">
      <rect class="label__ornament" x="-135" y="-96" width="270" height="26"/>
      <circle class="label__ornament" cx="0" cy="-76" r="32"/>
      <rect class="label__ornament" x="-14" y="-135" width="28" height="16"/>
    </g>
    <text class="label__title" x="0" y="25" text-anchor="middle" textLength="345" lengthAdjust="spacingAndGlyphs">Кельвана-Л</text>
    <rect class="label__rule" x="-176" y="49" width="352" height="52"/>
    <rect class="label__rule label__rule--thin" x="-166" y="56" width="332" height="38"/>
    <text class="label__spec" x="-94" y="80" text-anchor="middle">500 ml</text>
    <text class="label__spec" x="50" y="80">4.4 % <tspan class="label__spec-small">of alcohol</tspan></text>
    <circle class="label__brand-ring" cx="0" cy="94" r="40"/>
    <text class="label__brand-name" x="0" y="99" text-anchor="middle">KELVANA</text>
    <text class="label__arc-text label__variety"><textPath href="#arc-bottom" startOffset="50%" text-anchor="middle" textLength="278" lengthAdjust="spacingAndGlyphs">Kelvana-L | Honig Pilsner</textPath></text>
  </svg>

  <!-- Wiener Ale -->
  <svg class="label label--wiener" viewBox="-195 -221 390 442" aria-label="Kelvana-L Wiener Ale label">
    <path class="label__body" d="M -195 -104 A 221 221 0 0 1 195 -104 L 195 104 A 221 221 0 0 1 -195 104 Z"/>
    <path class="label__rule" d="M -169 -107 A 200 200 0 0 1 169 -107"/>
    <path class="label__rule label__rule--thin" d="M -162 -107 A 194 194 0 0 1 162 -107"/>
    <path class="label__rule label__rule--thin" d="M -80 -107 A 134 134 0 0 1 80 -107"/>
    <path class="label__rule" d="M -173 101 A 200 200 0 0 0 173 101"/>
    <path class="label__rule label__rule--thin" d="M -166 101 A 194 194 0 0 0 166 101"/>
    <path class="label__rule label__rule--thin" d="M -91 101 A 134 134 0 0 0 91 101"/>
    <text class="label__arc-text label__brewery"><textPath href="#arc-top" startOffset="50%" text-anchor="middle" textLength="240" lengthAdjust="spacing">FAMILY BREWERY</textPath></text>
    <rect class="label__rule" x="-176" y="-107" width="352" height="48"/>
    <rect class="label__rule label__rule--thin" x="-166" y="-100" width="332" height="34"/>
    <g role="img" aria-label="Crown, family monogram and foliate scroll ornament">
      <rect class="label__ornament" x="-135" y="-96" width="270" height="26"/>
      <circle class="label__ornament" cx="0" cy="-76" r="32"/>
      <rect class="label__ornament" x="-14" y="-135" width="28" height="16"/>
    </g>
    <text class="label__title" x="0" y="25" text-anchor="middle" textLength="345" lengthAdjust="spacingAndGlyphs">Кельвана-Л</text>
    <rect class="label__rule" x="-176" y="49" width="352" height="52"/>
    <rect class="label__rule label__rule--thin" x="-166" y="56" width="332" height="38"/>
    <text class="label__spec" x="-94" y="80" text-anchor="middle">500 ml</text>
    <text class="label__spec" x="50" y="80">4.4 % <tspan class="label__spec-small">of alcohol</tspan></text>
    <circle class="label__brand-ring" cx="0" cy="94" r="40"/>
    <text class="label__brand-name" x="0" y="99" text-anchor="middle">KELVANA</text>
    <text class="label__arc-text label__variety"><textPath href="#arc-bottom" startOffset="50%" text-anchor="middle" textLength="272" lengthAdjust="spacingAndGlyphs">Kelvana-L | Wiener Ale</textPath></text>
  </svg>

  <!-- Weissbier -->
  <svg class="label label--weiss" viewBox="-195 -221 390 442" aria-label="Kelvana-L Weissbier label">
    <path class="label__body" d="M -195 -104 A 221 221 0 0 1 195 -104 L 195 104 A 221 221 0 0 1 -195 104 Z"/>
    <path class="label__rule" d="M -169 -107 A 200 200 0 0 1 169 -107"/>
    <path class="label__rule label__rule--thin" d="M -162 -107 A 194 194 0 0 1 162 -107"/>
    <path class="label__rule label__rule--thin" d="M -80 -107 A 134 134 0 0 1 80 -107"/>
    <path class="label__rule" d="M -173 101 A 200 200 0 0 0 173 101"/>
    <path class="label__rule label__rule--thin" d="M -166 101 A 194 194 0 0 0 166 101"/>
    <path class="label__rule label__rule--thin" d="M -91 101 A 134 134 0 0 0 91 101"/>
    <text class="label__arc-text label__brewery"><textPath href="#arc-top" startOffset="50%" text-anchor="middle" textLength="240" lengthAdjust="spacing">FAMILY BREWERY</textPath></text>
    <rect class="label__rule" x="-176" y="-107" width="352" height="48"/>
    <rect class="label__rule label__rule--thin" x="-166" y="-100" width="332" height="34"/>
    <g role="img" aria-label="Crown, family monogram and foliate scroll ornament">
      <rect class="label__ornament" x="-135" y="-96" width="270" height="26"/>
      <circle class="label__ornament" cx="0" cy="-76" r="32"/>
      <rect class="label__ornament" x="-14" y="-135" width="28" height="16"/>
    </g>
    <text class="label__title" x="0" y="25" text-anchor="middle" textLength="345" lengthAdjust="spacingAndGlyphs">Кельвана-Л</text>
    <rect class="label__rule" x="-176" y="49" width="352" height="52"/>
    <rect class="label__rule label__rule--thin" x="-166" y="56" width="332" height="38"/>
    <text class="label__spec" x="-94" y="80" text-anchor="middle">500 ml</text>
    <text class="label__spec" x="50" y="80">4.4 % <tspan class="label__spec-small">of alcohol</tspan></text>
    <circle class="label__brand-ring" cx="0" cy="94" r="40"/>
    <text class="label__brand-name" x="0" y="99" text-anchor="middle">KELVANA</text>
    <text class="label__arc-text label__variety"><textPath href="#arc-bottom" startOffset="50%" text-anchor="middle" textLength="248" lengthAdjust="spacingAndGlyphs">Kelvana-L | Weissbier</textPath></text>
  </svg>

</main>
</body>
</html>
```